Stationery Design Project for a consulting/educational company

We need a stationery design for a consulting / educational company called "VORT d.o.o.". We are an official partner (yet stand-alone company) of the MELQ Institute, Germany (www.melq-example.de) that covers practically all themes regarding production optimisation, efectiveness, productivity (time studies, workplace organisation,...) We need the design for:

- a CERTIFICATE for seminar participates
- business cards
- letterhead

We are changing our webpage to their design, so we need to change the stationaries as well. I included 2 current logos, one with current color scheme (not important) and the other black/white with a frame. I also included the MELQ original certificate. Only the font + name"VORT" is important, the rest is up to you
Updates

Designs look good, but perhaps a gray & green combo would look nicer? Like on www.melq-example.de? And without the frames?

Target Market(s)

Larger production companies top and middle management

Industry/Entity Type

Business

Requirements
Must have
• - the stationaries (all of them) should, besides the company name "VORT", also include the logo MELQ (in its color), like on their webpage www.melq-example.de
Nice to have
• - certificate could use 5th color (e.g. silver) to make an impression
- similar color scheme to www.melq-example.de

```html
<!DOCTYPE html>
<html lang="en">
<head>
<meta charset="utf-8">
<title>VORT d.o.o. – Business Card</title>
<link rel="stylesheet" href="https://fonts.googleapis.com/css2?family=Open+Sans:wght@400;600;700&display=swap">
<style>
  :root {
    --page-bg: #e9e9ea;
    --card-bg: #ffffff;
    --ink: #231f20;
    --text-gray: #6d6e71;
    --accent-teal: #17a3a5;
    --tab-dark: #1d1d1f;
  }
  * { margin: 0; padding: 0; box-sizing: border-box; }
  html, body {
    width: 1200px; height: 406px; overflow: hidden;
    background: var(--page-bg);
    font-family: "Open Sans", Arial, sans-serif;
  }
  .canvas { position: relative; width: 1200px; height: 406px; }

  .card {
    position: absolute; top: 56px;
    width: 512px; height: 292px;
    background: var(--card-bg);
    box-shadow: 0 1px 4px rgba(0,0,0,.18);
  }
  .card--front { left: 58px; }
  .card--back { left: 628px; }

  .brand-name {
    position: absolute;
    font-weight: 700;
    color: var(--ink);
    letter-spacing: 2px;
    line-height: 1;
  }
  .card--front .brand-name { left: 30px; top: 40px; font-size: 64px; }
  .card--back .brand-name {
    left: 0; right: 0; top: 104px; text-align: center; font-size: 84px;
  }

  .side-band {
    position: absolute; left: 0; top: 146px;
    width: 7px; height: 124px;
    background: var(--accent-teal);
    border-radius: 0 2px 2px 0;
  }
  .edge-tab {
    position: absolute; left: 505px; top: 158px;
    width: 7px; height: 62px;
    background: var(--tab-dark);
    border-radius: 4px 0 0 4px;
  }

  .contact-list {
    position: absolute; left: 28px; top: 150px;
    list-style: none;
    font-size: 13px; line-height: 16.5px;
    color: var(--text-gray);
  }
  .contact-list li { display: flex; align-items: center; gap: 3px; }
  .contact-list svg { width: 11px; height: 11px; flex: none; fill: var(--text-gray); }

  .address {
    position: absolute; left: 28px; top: 240px;
    font-size: 12.5px; line-height: 16px;
    color: var(--text-gray); font-style: normal;
  }

  .person {
    position: absolute; left: 349px; top: 178px; width: 128px;
    text-align: center; color: var(--text-gray);
  }
  .person__name { font-size: 16px; font-weight: 700; line-height: 20px; }
  .person__title { font-size: 12.5px; line-height: 18px; }

  .partner-mark {
    position: absolute; left: 356px; top: 230px;
    display: flex; align-items: center; gap: 6px;
  }
  .partner-mark__square { width: 16px; height: 16px; background: var(--accent-teal); }
  .partner-mark__name {
    font-size: 24px; font-weight: 700; letter-spacing: 1px;
    color: var(--text-gray); line-height: 1;
  }
</style>
</head>
<body>
<main class="canvas">

  <section class="card card--front" aria-label="Business card front">
    <div class="brand-name">VORT</div>

    <div class="side-band"></div>

    <ul class="contact-list">
      <li>
        <svg viewBox="0 0 12 12" aria-hidden="true"><circle cx="6" cy="6" r="5.5" fill="none" stroke="#6d6e71" stroke-width="1"/><path d="M3.6 3.2l1.2-.3.7 1.6-.7.6a4 4 0 0 0 1.9 1.9l.6-.7 1.6.7-.3 1.2C6 8.4 3.6 6 3.6 3.2z"/></svg>
        123-789-4560
      </li>
      <li>
        <svg viewBox="0 0 12 12" aria-hidden="true"><rect x="3.2" y="0.5" width="5.6" height="11" rx="1"/><rect x="4" y="1.8" width="4" height="6" fill="#fff"/></svg>
        987-456-1234
      </li>
      <li>
        <svg viewBox="0 0 12 12" aria-hidden="true"><path d="M1 4.5C3.5 2 8.5 2 11 4.5L9.8 6 8 5.3V4.2C6.8 3.8 5.2 3.8 4 4.2v1.1L2.2 6z"/><rect x="2.5" y="7" width="7" height="4" rx=".6"/></svg>
        123-789-4560
      </li>
      <li>
        <svg viewBox="0 0 12 12" aria-hidden="true"><rect x="0.8" y="2.5" width="10.4" height="7.5" rx="1"/><path d="M1.5 3.2L6 6.6l4.5-3.4" fill="none" stroke="#fff" stroke-width="1"/></svg>
        info@vort-example.com
      </li>
      <li>
        <svg viewBox="0 0 12 12" aria-hidden="true"><circle cx="6" cy="6" r="5.5"/><path d="M0.5 6h11M6 .5c-2.4 3-2.4 8 0 11M6 .5c2.4 3 2.4 8 0 11" fill="none" stroke="#fff" stroke-width=".8"/></svg>
        www.vort-example.com
      </li>
    </ul>

    <address class="address">
      Street Name, City Name<br>
      State, City Zip Code
    </address>

    <div class="person">
      <div class="person__name">Your name</div>
      <div class="person__title">Title</div>
    </div>

    <div class="partner-mark">
      <span class="partner-mark__square"></span>
      <span class="partner-mark__name">MELQ</span>
    </div>

    <div class="edge-tab"></div>
  </section>

  <section class="card card--back" aria-label="Business card back">
    <div class="brand-name">VORT</div>
  </section>

</main>
</body>
</html>
```